Gourmet food made with love and care in my country kitchen

I'd like a business card designed for my small home-based food business. I have made labelling in federation blue for my food products (Labneh cheese, spicy pumpkin chutney, dukkah, caramelised onion jam, yo-Yo biscuits, chocolate mud cake etc) and have navy and white checked surrounds/borders on my brochures so would like to stick to these country colours.
Target Market(s)
Foodies who love gourmet delicacies. Everyone who enjoys a picnic that they don't have to prepare themselves.
Industry/Entity Type
Business
Contact Information for Business Card
Larkhollow Pantry
42 Tindale's Lane
Brimsworth Qld 4829
Phone Viv 07 48216597 or 0412386951
- Harrington

```html
<!DOCTYPE html>
<html lang="en">
<head>
<meta charset="utf-8">
<title>Larkhollow Pantry – Business Card</title>
<link rel="stylesheet" href="https://fonts.googleapis.com/css2?family=Macondo&family=Arimo&family=Cormorant+Garamond:ital,wght@1,500&display=swap">
<style>
  :root {
    --page: #ffffff;
    --card: #ffffff;
    --navy: #3a55a8;
    --federation-blue: #3d99d6;
    --text: #ffffff;
    --photo-food: linear-gradient(160deg, #cfd8c4 0%, #8a7a66 45%, #d9a766 70%, #3b3b3b 100%);
    --photo-field: linear-gradient(180deg, #c9dbe8 0%, #6f8f5a 40%, #4f7d34 75%, #3f6a2a 100%);
  }
  * { margin: 0; padding: 0; box-sizing: border-box; }
  html, body {
    width: 1200px; height: 1000px; overflow: hidden;
    background: var(--page);
  }
  .card {
    position: absolute; left: 45px; top: 150px;
    width: 1110px; height: 685px;
    background: var(--card);
  }
  .card-frame {
    position: absolute; left: 46px; top: 50px;
    width: 1014px; height: 583px;
    border: 7px solid var(--navy);
  }
  .card-panel {
    position: absolute; left: 63px; top: 66px;
    width: 980px; height: 552px;
    background: var(--federation-blue);
    color: var(--text);
  }
  .brand-name {
    position: absolute; left: 55px; top: 20px;
    font-family: "Macondo", cursive;
    font-weight: 400; font-size: 104px; line-height: 1;
    letter-spacing: 1px; white-space: nowrap;
  }
  .services {
    position: absolute; left: 145px; top: 160px;
    list-style: none;
    font-family: "Macondo", cursive;
    font-size: 38px; line-height: 50px; letter-spacing: 1px;
  }
  .services li::before {
    content: "•"; display: inline-block; width: 32px;
  }
  .photo { position: absolute; }
  .photo-food {
    left: 665px; top: 147px; width: 165px; height: 180px;
    background: var(--photo-food);
  }
  .photo-field {
    left: 151px; top: 317px; width: 217px; height: 160px;
    background: var(--photo-field);
  }
  .contact {
    position: absolute; left: 404px; top: 350px;
    font-family: "Arimo", Arial, sans-serif;
    font-size: 21px; line-height: 31.5px;
  }
  .tagline {
    position: absolute; left: 0; top: 486px; width: 1004px;
    text-align: center;
    font-family: "Cormorant Garamond", Georgia, serif;
    font-style: italic; font-weight: 500;
    font-size: 23px; line-height: 26px;
  }
</style>
</head>
<body>
  <div class="card">
    <div class="card-frame"></div>
    <div class="card-panel">
      <h1 class="brand-name">Larkhollow Pantry</h1>
      <ul class="services">
        <li>Gourmet market food</li>
        <li>Vintage Picnic Hampers</li>
        <li>Cooking Classes</li>
      </ul>
      <div class="photo photo-food" role="img" aria-label="Photo of a rustic berry galette on a cast-iron pan beside a bottle of olive oil on an outdoor table"></div>
      <div class="photo photo-field" role="img" aria-label="Photo of gum trees and a white fence beside green cane fields under a pale sky"></div>
      <address class="contact" style="font-style:normal">
        <p>&nbsp;42 Tindale's Lane, Mt Corran Via Brimsworth</p>
        <p>Email: larkhollowpantry@postmail.net</p>
        <p>Phone Viv: 07 48216597 or 0412386951</p>
        <p>Socials: Larkhollow Pantry</p>
      </address>
      <p class="tagline">Gourmet food made in my country kitchen, using fresh ingredients,<br>for your enjoyment and convenience. Viv Harrow</p>
    </div>
  </div>
</body>
</html>
```